Website design for Maple Nook Kidcare

I need a website designed for my daycare business, Maple Nook Kidcare, now that I have a new logo. My former website was ok but simple and I did not have a logo yet. It also was created by me using a template and was entirely pink. I loved the bright, happy feel of it but worried it might not appeal as much to potential clients who have sons. Therefore, I need a site which will appeal to both genders while still keeping the cheerful color scheme of my new logo, which has pinks, blue, green and cream.

Reason: Hello! I am still trying to download my new logo and am sorry it is taking me so long. Hopefully I will it posted by the end of today (US Eastern Standard Time). Thank you all very much for your patience!

Hello! I have finally managed to upload my new logo for you to use in designing my website. I'm sorry it took so long and greatly appreciate your time and creative efforts! I look forward to seeing what is submitted based on my logo design and its style/colors.

Many thanks!

Reason: As I've been traveling and posted my logo file late, I am extending my deadline. I am now back and can focus on providing more and better feedback. I appreciate your patience and submissions very much!

Reason: I need more time to provide feedback and make decisions.

Industry/Entity Type

Daycare

Colors
0192cd
33a6d7
86cae7
cadf82
fbf289
add136
e34197

```html
<!DOCTYPE html>
<html lang="en">
<head>
<meta charset="utf-8">
<title>Maple Nook Kidcare</title>
<link rel="stylesheet" href="https://fonts.googleapis.com/css2?family=Sansita:ital,wght@1,800&family=Signika:wght@400;600&family=Source+Sans+3:wght@400;600;700&display=swap">
<style>
:root{
  --blue:#1fa3d8;
  --blue-dark:#0192cd;
  --sky:#86cae7;
  --green:#add136;
  --green-soft:#b6d45a;
  --green-pale:#dbe9a6;
  --pink:#e34197;
  --pink-soft:#f09fcd;
  --cream:#fbf7ec;
  --text:#6b6b6b;
  --muted:#8a8a8a;
  --white:#ffffff;
}
*{margin:0;padding:0;box-sizing:border-box}
html,body{width:1024px;height:1200px;overflow:hidden;background:var(--white)}
body{position:relative;font-family:"Source Sans 3",sans-serif;color:var(--text)}
.abs{position:absolute}

/* header */
.brand{left:137px;top:14px;font-family:"Signika",sans-serif;font-weight:600;font-size:27px;line-height:28px;color:var(--blue)}
.contact-strip{top:24px;left:440px;display:flex;font-size:11px;color:var(--muted);height:26px;align-items:center}
.contact-strip .item{display:flex;align-items:center;gap:8px;padding:0 14px;border-left:1px solid #e6e6e6;height:26px}
.contact-strip .item:last-child{padding-right:0}

/* nav */
.main-nav{left:135px;top:76px;width:752px;height:40px;background:var(--green-soft);border:1px solid #a4c63f;display:flex;align-items:stretch;z-index:3}
.main-nav a{font-family:"Signika",sans-serif;font-weight:600;font-size:13px;color:var(--white);text-decoration:none;display:flex;align-items:center;padding:0 17px}
.main-nav a.active{background:var(--pink);padding:0 22px 0 29px}
.main-nav a:nth-child(2){padding-left:21px}

/* hero */
.hero{left:0;top:92px;width:1024px;height:496px;background:linear-gradient(100deg,#f3f1ee 0%,#ece7e3 32%,#d9b9a2 52%,#c49574 70%,#e8dccd 88%,#f0e6dc 100%)}
.hero-top-wave,.hero-bottom-wave,.footer-wave{left:0;width:1024px}
.hero-title{left:139px;top:244px;font-family:"Sansita",sans-serif;font-style:italic;font-weight:800;font-size:27px;line-height:33px;color:var(--blue)}
.hero-sub{left:143px;top:323px;font-size:18px;line-height:23px;color:var(--pink)}

/* feature cards */
.card{top:470px;width:240px;height:254px;border:1px solid rgba(0,0,0,.06);z-index:2}
.card h2{font-family:"Sansita",sans-serif;font-style:italic;font-weight:800;font-size:19px;color:var(--white);text-align:center;margin-top:13px;letter-spacing:.5px}
.card .photo{position:absolute;left:15px;top:53px;width:208px;height:99px}
.card p{position:absolute;left:15px;top:168px;width:214px;font-size:9.6px;line-height:14.5px;font-weight:700;color:var(--white)}
.card.learning{left:136px;background:var(--sky)}
.card.creativity{left:392px;background:#b5d65a}
.card.sharing{left:649px;background:var(--pink-soft)}

/* welcome */
.welcome-photo{left:138px;top:770px;width:111px;height:167px;background:linear-gradient(160deg,#8a6a50,#d4b49a 55,#e9d6c6)}
.section-title{font-family:"Sansita",sans-serif;font-style:italic;font-weight:800;font-size:16px;color:var(--blue)}
.welcome-title{left:264px;top:766px}
.welcome-copy{left:264px;top:801px;width:360px;font-size:9.2px;line-height:14.5px;color:var(--muted)}
.welcome-copy p+p{margin-top:14px}
.welcome-copy strong{color:#6b6b6b;font-weight:700}
.read-more{font-size:7.5px;font-weight:700;color:var(--blue);text-decoration:underline}
.welcome-more{left:264px;top:918px}

.news-title{left:649px;top:764px}
.news-item{left:649px;width:250px;height:70px}
.news-date{position:absolute;left:0;top:0;width:47px;height:46px;background:var(--pink-soft);color:var(--white);text-align:center}
.news-date b{display:block;font-weight:400;font-size:17px;line-height:17px;margin-top:8px}
.news-date span{font-size:6.5px}
.news-text{position:absolute;left:64px;top:-3px;width:186px;font-size:12px;line-height:20px;color:var(--muted)}
.news-text .read-more{text-decoration:none;font-size:7px}

/* footer */
.footer{left:0;top:997px;width:1024px;height:168px;background:#b2d25a}
.footer-brand{left:137px;top:1054px;font-family:"Signika",sans-serif;font-weight:600;font-size:20px;line-height:21px;color:var(--white)}
.footer-col{top:1028px;color:var(--white)}
.footer-col h3{font-family:"Signika",sans-serif;font-weight:600;font-size:12px;margin-bottom:11px;color:#f1f7dc}
.footer-col li{list-style:none;font-size:9.5px;line-height:19.2px;font-family:"Signika",sans-serif}
.footer-col li::before{content:"›";color:#dfeeb0;margin-right:8px}
.footer-col.contact li::before{content:none}
.footer-col.contact li{display:flex;align-items:center;gap:9px;line-height:24px}
.map{left:761px;top:1052px;width:127px;height:81px;background:linear-gradient(135deg,#eeeeea,#dcdcd6 50%,#cfd8e6)}
.bottom-bar{left:0;top:1165px;width:1024px;height:35px;background:var(--green-pale);font-size:9.5px;color:#9aa37c}
.bottom-bar .copy{position:absolute;left:136px;top:12px}
.bottom-bar .legal{position:absolute;right:160px;top:12px}
</style>
</head>
<body>

<header>
  <div class="abs brand">Maple Nook<br>Kidcare</div>
  <div class="abs contact-strip">
    <div class="item">
      <svg width="14" height="14" viewBox="0 0 14 14"><circle cx="7" cy="7.5" r="5" fill="none" stroke="#add136" stroke-width="1.6"/><path d="M7 5v3h2" stroke="#add136" stroke-width="1.4" fill="none"/><path d="M2 3l2-2M12 3l-2-2" stroke="#add136" stroke-width="1.4"/></svg>
      (Mon - Fri) 8:00AM to 6:00PM
    </div>
    <div class="item">
      <svg width="22" height="12" viewBox="0 0 22 12"><rect x="7" y="1" width="14" height="10" fill="none" stroke="#add136" stroke-width="1.3"/><path d="M7 1l7 6 7-6" fill="none" stroke="#add136" stroke-width="1.3"/><path d="M0 3h5M2 6h4M1 9h5" stroke="#add136" stroke-width="1"/></svg>
      hello@maplenookkids.com
    </div>
    <div class="item">
      <svg width="13" height="13" viewBox="0 0 13 13"><path d="M3 1l2 3-1.3 1.3c.7 1.6 2 2.9 3.6 3.6L8.6 7.6l3 2-1.2 2.2C5.6 11.4 1.6 7.4 1 2.3z" fill="#add136"/></svg>
      +(555) 014-2290
    </div>
  </div>
  <nav class="abs main-nav">
    <a class="active" href="#">Home</a>
    <a href="#">About Us</a>
    <a href="#">Services</a>
    <a href="#">Hours and Fees</a>
    <a href="#">Policies</a>
    <a href="#">Photos</a>
    <a href="#">Testimonials</a>
    <a href="#">Contact Us</a>
  </nav>
</header>

<section>
  <div class="abs hero" role="img" aria-label="Photo of three laughing toddlers hugging in a bright playroom with toys and a wooden rocking horse"></div>
  <svg class="abs hero-top-wave" style="top:88px" height="14" viewBox="0 0 1024 14" preserveAspectRatio="none">
    <path d="M0 0H1024V6 Q1017 14 1010 6 T996 6 T982 6 T968 6 T954 6 T940 6 T926 6 T912 6 T898 6 T884 6 T870 6 T856 6 T842 6 T828 6 T814 6 T800 6 T786 6 T772 6 T758 6 T744 6 T730 6 T716 6 T702 6 T688 6 T674 6 T660 6 T646 6 T632 6 T618 6 T604 6 T590 6 T576 6 T562 6 T548 6 T534 6 T520 6 T506 6 T492 6 T478 6 T464 6 T450 6 T436 6 T422 6 T408 6 T394 6 T380 6 T366 6 T352 6 T338 6 T324 6 T310 6 T296 6 T282 6 T268 6 T254 6 T240 6 T226 6 T212 6 T198 6 T184 6 T170 6 T156 6 T142 6 T128 6 T114 6 T100 6 T86 6 T72 6 T58 6 T44 6 T30 6 T16 6 T0 6Z" fill="#fff"/>
  </svg>
  <svg class="abs hero-bottom-wave" style="top:576px" height="14" viewBox="0 0 1024 14" preserveAspectRatio="none">
    <path d="M0 14H1024V8 Q1017 0 1010 8 T996 8 T982 8 T968 8 T954 8 T940 8 T926 8 T912 8 T898 8 T884 8 T870 8 T856 8 T842 8 T828 8 T814 8 T800 8 T786 8 T772 8 T758 8 T744 8 T730 8 T716 8 T702 8 T688 8 T674 8 T660 8 T646 8 T632 8 T618 8 T604 8 T590 8 T576 8 T562 8 T548 8 T534 8 T520 8 T506 8 T492 8 T478 8 T464 8 T450 8 T436 8 T422 8 T408 8 T394 8 T380 8 T366 8 T352 8 T338 8 T324 8 T310 8 T296 8 T282 8 T268 8 T254 8 T240 8 T226 8 T212 8 T198 8 T184 8 T170 8 T156 8 T142 8 T128 8 T114 8 T100 8 T86 8 T72 8 T58 8 T44 8 T30 8 T16 8 T0 8Z" fill="#fff"/>
  </svg>
  <h1 class="abs hero-title">Welcome to<br>Maple Nook Kidcare</h1>
  <p class="abs hero-sub">a playspace where children can<br>play, create, and imagine!</p>
</section>

<section>
  <article class="abs card learning">
    <h2>LEARNING</h2>
    <div class="photo" role="img" aria-label="Photo of children building with colourful blocks at a table" style="background:linear-gradient(120deg,#e8b07a,#f2d39a 45%,#7cc0e0)"></div>
    <p>We develop age-appropriate activities that introduce and strengthen academic and social skills.</p>
  </article>
  <article class="abs card creativity">
    <h2>CREATIVITY</h2>
    <div class="photo" role="img" aria-label="Photo of a child with painted cheeks holding up paint-covered hands" style="background:linear-gradient(120deg,#3f5a2e,#d9a98c 45%,#6a3fa0 75%,#3f5a2e)"></div>
    <p>We offer children a wide range of creative opportunities including art projects, toddler yoga lessons, afternoon tea parties, dress up play, and a large selection of books and games.</p>
  </article>
  <article class="abs card sharing">
    <h2>SHARING</h2>
    <div class="photo" role="img" aria-label="Photo of a child and a woman laughing over a pink toy tea set" style="background:linear-gradient(120deg,#8a6a52,#d7b7a0 40%,#e88aa8 60%,#b8846a)"></div>
    <p>We strive to include enrichment activities that extend your child's understanding of the world and their role in it.</p>
  </article>
</section>

<section>
  <div class="abs welcome-photo" role="img" aria-label="Photo of a smiling caregiver with a young girl"></div>
  <h2 class="abs section-title welcome-title">Welcome to Maple Nook Kidcare!</h2>
  <div class="abs welcome-copy">
    <p>We are a <strong>licensed Group Family Day Care</strong>, located in Riverton's leafy Eastgate district. We are located on a pretty, tree-lined block on Linden Row, between Oak and Birch Avenues. We are a few blocks from the Green Line tram and the Route 12 bus line, and we offer flexible hourly childcare, making it as easy as possible for busy parents on the go to arrange their children's care.</p>
    <p>We invite you to learn more about us and hope you will visit us soon</p>
  </div>
  <a class="abs read-more welcome-more" href="#">READ MORE</a>

  <h2 class="abs section-title news-title">Latest News</h2>
  <div class="abs news-item" style="top:801px">
    <div class="news-date"><b>05</b><span>May 2014</span></div>
    <p class="news-text">We are thrilled to have found a new cheerful space with a private backyard... <a class="read-more" href="#">▸READ MORE</a></p>
  </div>
  <div class="abs news-item" style="top:874px">
    <div class="news-date"><b>05</b><span>May 2014</span></div>
    <p class="news-text">We are thrilled to have found a new cheerful space with a private backyard... <a class="read-more" href="#">▸READ MORE</a></p>
  </div>
</section>

<footer>
  <svg class="abs footer-wave" style="top:985px" height="14" viewBox="0 0 1024 14" preserveAspectRatio="none">
    <path d="M0 14H1024V8 Q1017 0 1010 8 T996 8 T982 8 T968 8 T954 8 T940 8 T926 8 T912 8 T898 8 T884 8 T870 8 T856 8 T842 8 T828 8 T814 8 T800 8 T786 8 T772 8 T758 8 T744 8 T730 8 T716 8 T702 8 T688 8 T674 8 T660 8 T646 8 T632 8 T618 8 T604 8 T590 8 T576 8 T562 8 T548 8 T534 8 T520 8 T506 8 T492 8 T478 8 T464 8 T450 8 T436 8 T422 8 T408 8 T394 8 T380 8 T366 8 T352 8 T338 8 T324 8 T310 8 T296 8 T282 8 T268 8 T254 8 T240 8 T226 8 T212 8 T198 8 T184 8 T170 8 T156 8 T142 8 T128 8 T114 8 T100 8 T86 8 T72 8 T58 8 T44 8 T30 8 T16 8 T0 8Z" fill="#b2d25a"/>
  </svg>
  <div class="abs footer"></div>
  <div class="abs footer-brand">Maple Nook<br>Kidcare</div>
  <div class="abs footer-col" style="left:310px">
    <h3>Navigation</h3>
    <ul><li>Home</li><li>About</li><li>Services</li><li>Contact</li></ul>
  </div>
  <div class="abs footer-col" style="left:439px">
    <h3>Links</h3>
    <ul><li>Menu1</li><li>Menu1</li><li>Menu1</li><li>Menu1</li></ul>
  </div>
  <div class="abs footer-col contact" style="left:565px">
    <h3 style="margin-bottom:5px">Contact Us</h3>
    <ul>
      <li><svg width="11" height="11" viewBox="0 0 13 13"><path d="M3 1l2 3-1.3 1.3c.7 1.6 2 2.9 3.6 3.6L8.6 7.6l3 2-1.2 2.2C5.6 11.4 1.6 7.4 1 2.3z" fill="#d3e69a"/></svg>+1800-123-4567</li>
      <li><svg width="11" height="9" viewBox="0 0 11 9"><rect width="11" height="9" fill="#d3e69a"/><path d="M0 0l5.5 5 5.5-5" fill="none" stroke="#b2d25a"/></svg>info@yourwebsite.com</li>
      <li style="align-items:flex-start;line-height:19px;margin-top:3px"><svg width="11" height="13" viewBox="0 0 11 13" style="margin-top:3px"><path d="M5.5 0A4.5 4.5 0 0 0 1 4.5C1 8 5.5 13 5.5 13S10 8 10 4.5A4.5 4.5 0 0 0 5.5 0z" fill="#d3e69a"/><circle cx="5.5" cy="4.5" r="1.6" fill="#b2d25a"/></svg><span>Address, Your Country<br>Your Zip Code</span></li>
    </ul>
  </div>
  <div class="abs footer-col" style="left:760px">
    <h3>Visit Us</h3>
  </div>
  <div class="abs map" role="img" aria-label="Street map showing the daycare location"></div>
  <div class="abs bottom-bar">
    <span class="copy">Copyright 2014 © CompanyName - All Rights Reserved</span>
    <span class="legal">Site Map &nbsp;•&nbsp; Privacy Policy</span>
  </div>
</footer>

</body>
</html>
```